Aviation Banner Ad Designs

SkyLedgerMetrics provides access to the most accurate aircraft operating cost information, to compare Piston, Turboprop and Jet aircraft.

The banners ads will be used for retargeting/remarketing - to bring visitors back to the site. The banners should remind and reinforce the key messages of what the site provides.

Target Market(s)

Private aircraft buyers including:
- Aircraft Brokers
- Charter Operators
- Corporate Flight Departments
- Aircraft Management companies
- Financial Institutions
- Aircraft Owners
- Prospective Buyers

Requirements
Must have
• A. Banner Objective
The visual and textual content of the banner should remind the viewer about the features of the site, and prompt them to return to the site.
1. Arresting visual
2. Headline
3. Single message
4. Compelling CTA
5. Logo - big enough to see
6. Standard DWR ad sizes/specs

B. Design Elements
Logo: As attached
Main Title: Calculate Jet Operating Costs
Subtitle: Compare Ownership Usage Scenarios
Call to Action Button: Compare Ownership Costs
Background: Several images supplied as options

C. Banner Sizes
Do examples as 300×250 , 728×90 , 160×600
Final sizes to also include 320×100 , 336x280 , 300x600

Finally delivery as .jpg files.

Font - use same font as on site

```html
<!DOCTYPE html>
<html lang="en">
<head>
<meta charset="utf-8">
<title>SkyLedgerMetrics – Jet Operating Costs Banner</title>
<link rel="stylesheet" href="https://fonts.googleapis.com/css2?family=Oswald:wght@500;600&family=Roboto:wght@500&display=swap">
<style>
  :root {
    --sky-light: #b3cde8;
    --sky-deep: #86acd8;
    --navy: #1b2330;
    --brand-red: #d92a2c;
    --white: #ffffff;
    --photo-sky: #c9d9ea;
    --photo-jet: #8da3bb;
    --photo-sunset: #d9a57b;
    --photo-cargo: #aab6c2;
  }
  html, body {
    margin: 0;
    padding: 0;
    overflow: hidden;
    background: var(--white);
  }
  .banner {
    position: relative;
    width: 1200px;
    height: 148px;
    overflow: hidden;
    background: var(--sky-light);
    font-family: "Oswald", sans-serif;
  }
  .banner__backdrop {
    position: absolute;
    inset: 0;
  }
  .brand {
    position: absolute;
    left: 22px;
    top: 52px;
    display: flex;
    align-items: center;
    gap: 10px;
  }
  .brand__mark {
    width: 22px;
    height: 22px;
    background: var(--brand-red);
  }
  .brand__name {
    font-family: "Oswald", sans-serif;
    font-weight: 500;
    font-size: 28px;
    color: var(--navy);
    letter-spacing: 0.5px;
  }
  .headline {
    position: absolute;
    left: 343px;
    top: 24px;
    margin: 0;
    font-weight: 600;
    font-size: 37px;
    line-height: 48px;
    color: var(--navy);
  }
  .headline__rank {
    text-decoration: underline;
    text-decoration-color: var(--brand-red);
    text-decoration-thickness: 3px;
    text-underline-offset: 4px;
  }
  .cta {
    position: absolute;
    left: 844px;
    top: 49px;
    width: 263px;
    height: 53px;
    display: flex;
    align-items: center;
    justify-content: center;
    background: var(--brand-red);
    color: var(--white);
    font-family: "Roboto", sans-serif;
    font-weight: 500;
    font-size: 21px;
    border-radius: 3px;
    box-shadow: 0 2px 4px rgba(0,0,0,0.25);
    text-decoration: none;
  }
  .photo {
    position: absolute;
    border-radius: 50%;
    border: 3px solid var(--white);
    box-sizing: border-box;
  }
  .photo--cargo {
    left: 257px; top: 92px; width: 72px; height: 72px;
    background: linear-gradient(160deg, var(--photo-sky), var(--photo-cargo));
  }
  .photo--jet {
    left: 694px; top: 55px; width: 88px; height: 88px;
    background: radial-gradient(circle at 50% 45%, #e8eef4, var(--photo-jet) 70%);
  }
  .photo--sunset {
    left: 1065px; top: -11px; width: 72px; height: 72px;
    background: linear-gradient(180deg, #f0c79c, var(--photo-sunset));
  }
  .icon-dollar {
    position: absolute;
    left: 1154px;
    top: 91px;
    width: 66px;
    height: 66px;
  }
</style>
</head>
<body>
  <div class="banner">
    <svg class="banner__backdrop" width="1200" height="148" viewBox="0 0 1200 148" aria-hidden="true">
      <path d="M560 148 C610 110 650 70 720 40 C800 8 880 20 960 8 C1040 -4 1100 0 1200 0 L1200 148 Z" fill="var(--sky-deep)"/>
    </svg>

    <div class="brand">
      <span class="brand__mark"></span>
      <span class="brand__name">SkyLedgerMetrics</span>
    </div>

    <div class="photo photo--cargo" role="img" aria-label="Cargo aircraft parked on the apron"></div>

    <h1 class="headline">The <span class="headline__rank">#1</span> to calculate<br>Jet operating costs</h1>

    <div class="photo photo--jet" role="img" aria-label="Business jet seen head-on"></div>

    <a class="cta" href="#">Request a Demo</a>

    <div class="photo photo--sunset" role="img" aria-label="Private jet flying at sunset"></div>

    <svg class="icon-dollar" viewBox="0 0 66 66" role="img" aria-label="Cost">
      <circle cx="33" cy="33" r="31" fill="var(--white)" stroke="var(--sky-deep)" stroke-width="2"/>
      <text x="33" y="43" text-anchor="middle" font-family="Roboto, sans-serif" font-weight="500" font-size="30" fill="var(--navy)">$</text>
    </svg>
  </div>
</body>
</html>
```